Business card design needed

Bright Path Ahead is an online wellness program designed for people dealing with cancer to take control of their lives and Bright path ahead.

Target Market(s)

initially woman aged 35 to 65 years eventaully then men

Industry/Entity Type

Business

Contact Information for Business Card

Marisol Dunkerly
Bright path ahead Coach
Marisol@brightpathahead.com.au
M 0419382716
Skype Marisol.Dunkerly
local number to come
www.brightpathahead.com.au

Requirements
Must have
• Business cards want to have a photo of me on the back this is a head shot. Also a small blurb " Marisol recovered and survived 2 types of cancer. She under went a transformational 12 month journey to overcome cancer naturally . Join her online coaching program to Bright path ahead.

Phone number and email and skype address.
Nice to have
• Looking for something that resembles health EG abstract tree of life, or something resembling health and balance . Like lime green/apple green want modern fresh. Want only 2 colours used on the cards. Need to use the logo and Bright path ahead on website and email signature - Clean and fresh

Also would like Letter head and logo for website and email signature

```html
<!DOCTYPE html>
<html lang="en">
<head>
<meta charset="utf-8">
<title>Bright Path Ahead – Business Card</title>
<link rel="stylesheet" href="https://fonts.googleapis.com/css2?family=Open+Sans:wght@400;600&family=Caveat:wght@500&display=swap">
<style>
  :root {
    --backdrop: #e6e8e4;
    --card: #fbfbf9;
    --green: #7bb23a;
    --green-deep: #5f9a2a;
    --ink: #3b3b3b;
    --rule: #d9dccf;
    --photo-top: #e9d6b8;
    --photo-mid: #c99a72;
    --photo-low: #3fa8a6;
  }
  * { box-sizing: border-box; margin: 0; padding: 0; }
  html, body {
    width: 1200px; height: 1200px; overflow: hidden;
    background: var(--backdrop);
    font-family: "Open Sans", Arial, sans-serif;
    color: var(--ink);
  }
  .canvas { position: relative; width: 1200px; height: 1200px; }
  .card {
    position: absolute; left: 250px;
    width: 700px; height: 400px;
    background: var(--card);
    box-shadow: 0 10px 30px rgba(0,0,0,0.15);
    overflow: hidden;
  }
  .card--front { top: 140px; }
  .card--back { top: 660px; }

  .brand-name {
    position: absolute;
    font-family: "Open Sans", Arial, sans-serif;
    font-weight: 600;
    color: var(--green);
    line-height: 1.05;
    letter-spacing: 0.5px;
  }
  .card--front .brand-name { left: 360px; top: 100px; font-size: 38px; width: 280px; }
  .card--back .brand-name { left: 70px; top: 185px; font-size: 44px; width: 280px; }

  .portrait {
    position: absolute; left: 150px; top: 110px;
    width: 170px; height: 195px;
    border-radius: 80px 80px 6px 6px;
    background: linear-gradient(180deg, var(--photo-top) 0%, var(--photo-mid) 55%, var(--photo-low) 100%);
  }
  .blurb {
    position: absolute; left: 360px; top: 205px;
    width: 290px;
    font-size: 12.5px; line-height: 19px;
    color: var(--ink);
  }

  .divider {
    position: absolute; left: 385px; top: 40px;
    width: 1px; height: 320px; background: var(--rule);
  }
  .holder { position: absolute; right: 60px; top: 58px; text-align: right; width: 240px; }
  .holder__name {
    font-family: "Caveat", cursive;
    font-size: 36px; color: var(--green); line-height: 1;
    white-space: nowrap;
  }
  .holder__role { font-size: 13px; color: var(--ink); margin-top: 4px; }

  .contact { position: absolute; left: 420px; top: 250px; list-style: none; font-size: 13px; line-height: 22px; }
  .contact__label { color: var(--green-deep); }
</style>
</head>
<body>
<main class="canvas">
  <section class="card card--front">
    <div class="portrait" role="img" aria-label="Head-and-shoulders portrait of the coach"></div>
    <div class="brand-name">Bright Path Ahead</div>
    <p class="blurb">Marisol recovered and survived 2 types of cancer. She underwent a transformational 12 month journey to overcome cancer naturally. Join her online coaching program to Bright path ahead.</p>
  </section>

  <section class="card card--back">
    <div class="brand-name">Bright Path Ahead</div>
    <div class="divider"></div>
    <div class="holder">
      <div class="holder__name">Marisol Dunkerly</div>
      <div class="holder__role">Bright path ahead Coach</div>
    </div>
    <ul class="contact">
      <li><span class="contact__label">Phone:</span> 0419382716</li>
      <li><span class="contact__label">Skype:</span> Marisol.Dunkerly</li>
      <li><span class="contact__label">Email:</span> Marisol@brightpathahead.com.au</li>
      <li><span class="contact__label">Website:</span> www.brightpathahead.com.au</li>
    </ul>
  </section>
</main>
</body>
</html>
```